DEIJ Annual Progress Report

We need a Word-based year-end progress report for The Halvorsen Circle, Inc. for their client Bramblewood Care Network. The report should be easily editable because this report represents the first draft. We want the report to use The Halvorsen Circle, Inc.'s colors as the main color and incorporate the client's colors as ascents. Please provide two spots per page where photos can be inserted.
Updates

Please include an introduction and conclusion paragraph. I will add that text later.

I uploaded the introduction and conclusion to use with the report.

Give some designer a chance to response, or update their designs.

Target Market(s)

Healthcare Executives

Industry/Entity Type

Healthcare consulting

Font styles to use
Other font styles liked:
• Loto, and Raleway

Requirements
Must have
• Use of the THC and BCN logos, appropriate photos in case I go with stock photos
Nice to have
• Warm but professional feeling
Should not have
• Cartoons, silly or funny pictures

```html
<!DOCTYPE html>
<html lang="en">
<head>
<meta charset="utf-8">
<title>The Halvorsen Circle, Inc. – 2023 Progress Report</title>
<link rel="stylesheet" href="https://fonts.googleapis.com/css2?family=Montserrat:wght@500;700;900&family=Poppins:wght@400;500;600;700&display=swap">
<style>
  :root {
    --backdrop: #d9d8d8;
    --navy: #23205e;
    --navy-deep: #1a1745;
    --gold: #b07d22;
    --gold-soft: #c9953a;
    --paper: #f2f2f2;
    --ink: #1c1c28;
    --white: #ffffff;
  }
  * { box-sizing: border-box; margin: 0; padding: 0; }
  html, body { width: 898px; height: 1200px; overflow: hidden; }
  body {
    background: var(--backdrop);
    font-family: "Poppins", sans-serif;
    color: var(--ink);
    position: relative;
  }
  .spread {
    position: absolute;
    left: 59px;
    width: 780px;
    height: 552px;
    overflow: hidden;
    box-shadow: 0 10px 24px rgba(0,0,0,.18);
  }
  .spread--cover { top: 32px; }
  .spread--inside { top: 616px; }
  .spread__art { position: absolute; inset: 0; width: 100%; height: 100%; display: block; }

  /* brand lock-up */
  .brand { position: absolute; display: flex; align-items: center; gap: 8px; }
  .brand__dot { width: 26px; height: 26px; border-radius: 50%; background: var(--navy); flex: none; }
  .brand__name {
    font-family: "Montserrat", sans-serif; font-weight: 900; color: var(--navy);
    font-size: 11px; line-height: 1.1; text-transform: uppercase; letter-spacing: .02em;
  }
  .brand__tagline { font-size: 6px; color: var(--gold); margin-top: 2px; font-weight: 500; text-transform: none; letter-spacing: 0; }

  /* back cover */
  .back-cover__brand { left: 42px; top: 372px; }
  .back-cover__contacts { position: absolute; left: 42px; top: 420px; }
  .contact-icons { display: flex; gap: 10px; margin-bottom: 8px; }
  .contact-icons span { width: 16px; height: 16px; border-radius: 50%; background: var(--gold); display: grid; place-items: center; }
  .contact-line { font-family: "Montserrat", sans-serif; font-weight: 500; font-size: 15px; color: var(--ink); line-height: 1.35; }

  /* front cover */
  .front-cover__brand { left: 560px; top: 62px; }
  .front-cover__year {
    position: absolute; left: 560px; top: 104px;
    font-family: "Montserrat", sans-serif; font-weight: 500; font-size: 40px; color: var(--gold); letter-spacing: .04em;
  }
  .front-cover__title {
    position: absolute; left: 520px; top: 152px;
    font-family: "Montserrat", sans-serif; font-weight: 900; font-size: 40px; line-height: .95; color: var(--navy-deep);
    text-transform: uppercase;
  }
  .front-cover__web {
    position: absolute; left: 390px; width: 390px; bottom: 40px; text-align: center;
    font-family: "Montserrat", sans-serif; font-size: 14px; letter-spacing: .22em; color: var(--white);
  }

  /* inside spread */
  .section-badge {
    position: absolute; left: 70px; top: 208px; width: 200px; text-align: center;
    font-family: "Montserrat", sans-serif; font-weight: 900; font-size: 30px; color: var(--white);
  }
  .timeline { position: absolute; left: 420px; top: 50px; width: 340px; }
  .timeline__item { position: relative; padding-left: 86px; height: 158px; }
  .timeline__heading {
    font-family: "Poppins", sans-serif; font-weight: 700; font-size: 15px; color: var(--ink); line-height: 1.2;
    margin: 14px 0 6px;
  }
  .timeline__list { list-style: none; }
  .timeline__list li {
    position: relative; padding-left: 16px; font-size: 10px; line-height: 1.35; margin-bottom: 3px; color: var(--ink);
  }
  .timeline__list li::before {
    content: ""; position: absolute; left: 0; top: 3px; width: 8px; height: 8px;
    border: 1.2px solid var(--navy); border-radius: 50%;
  }
  .timeline__list li::after {
    content: ""; position: absolute; left: 2.5px; top: 5.2px; width: 3px; height: 1.6px;
    border-left: 1.2px solid var(--navy); border-bottom: 1.2px solid var(--navy); transform: rotate(-45deg);
  }
  .timeline__icon { position: absolute; left: 0; top: 0; width: 66px; height: 66px; }
</style>
</head>
<body>

<section class="spread spread--cover">
  <svg class="spread__art" viewBox="0 0 780 552" aria-hidden="false">
    <defs>
      <linearGradient id="meeting-room" x1="0" y1="0" x2="1" y2="1">
        <stop offset="0" stop-color="#0f1620"/>
        <stop offset=".35" stop-color="#2c3d3d"/>
        <stop offset=".6" stop-color="#6b6558"/>
        <stop offset=".8" stop-color="#3a3a38"/>
        <stop offset="1" stop-color="#151a22"/>
      </linearGradient>
      <clipPath id="back-page"><rect x="0" y="0" width="390" height="552"/></clipPath>
      <clipPath id="front-page"><rect x="390" y="0" width="390" height="552"/></clipPath>
    </defs>
    <g role="img" aria-label="Photo: silhouettes of a team meeting in a glass-walled city office">
      <rect width="780" height="552" fill="url(#meeting-room)"/>
    </g>
    <g clip-path="url(#back-page)">
      <circle cx="70" cy="470" r="236" fill="var(--navy)"/>
      <circle cx="30" cy="490" r="220" fill="var(--paper)"/>
      <circle cx="60" cy="470" r="262" fill="none" stroke="#ffffff" stroke-width="1.2" opacity=".8"/>
    </g>
    <g clip-path="url(#front-page)">
      <circle cx="640" cy="150" r="248" fill="var(--gold)" opacity=".93"/>
      <circle cx="670" cy="118" r="220" fill="var(--paper)"/>
      <circle cx="620" cy="190" r="282" fill="none" stroke="#ffffff" stroke-width="1.2" opacity=".8"/>
    </g>
    <line x1="390" y1="0" x2="390" y2="552" stroke="#000" stroke-opacity=".2"/>
  </svg>

  <div class="brand back-cover__brand">
    <span class="brand__dot"></span>
    <div class="brand__name">The Halvorsen<br>Circle, Inc.<div class="brand__tagline">Lasting solutions for equity and inclusion</div></div>
  </div>
  <div class="back-cover__contacts">
    <div class="contact-icons">
      <span><svg width="9" height="9" viewBox="0 0 24 24"><path d="M6.6 10.8a15 15 0 0 0 6.6 6.6l2.2-2.2a1 1 0 0 1 1-.25 11.4 11.4 0 0 0 3.6.57 1 1 0 0 1 1 1V20a1 1 0 0 1-1 1A17 17 0 0 1 3 4a1 1 0 0 1 1-1h3.5a1 1 0 0 1 1 1c0 1.25.2 2.45.57 3.57a1 1 0 0 1-.25 1z" fill="#fff"/></svg></span>
      <span><svg width="9" height="9" viewBox="0 0 24 24"><circle cx="12" cy="12" r="9" fill="none" stroke="#fff" stroke-width="2"/><path d="M3 12h18M12 3c3 3 3 15 0 18M12 3c-3 3-3 15 0 18" fill="none" stroke="#fff" stroke-width="1.6"/></svg></span>
    </div>
    <p class="contact-line">1234567890</p>
    <p class="contact-line">www.yourwebsite.com</p>
  </div>

  <div class="brand front-cover__brand">
    <span class="brand__dot"></span>
    <div class="brand__name">The Halvorsen<br>Circle, Inc.<div class="brand__tagline">Lasting solutions for equity and inclusion</div></div>
  </div>
  <p class="front-cover__year">2023</p>
  <h1 class="front-cover__title">Progress<br>Report</h1>
  <p class="front-cover__web">www.yourwebsite.com</p>
</section>

<section class="spread spread--inside">
  <svg class="spread__art" viewBox="0 0 780 552">
    <defs>
      <linearGradient id="handshake" x1="0" y1="0" x2="1" y2="1">
        <stop offset="0" stop-color="#f1e3c6"/>
        <stop offset=".4" stop-color="#c99a78"/>
        <stop offset=".7" stop-color="#d9b894"/>
        <stop offset="1" stop-color="#ead9b8"/>
      </linearGradient>
      <clipPath id="photo-page"><rect x="0" y="0" width="390" height="552"/></clipPath>
    </defs>
    <g role="img" aria-label="Photo: two people shaking hands, softly blurred warm background">
      <rect width="390" height="552" fill="url(#handshake)"/>
    </g>
    <rect x="390" y="0" width="390" height="552" fill="var(--paper)"/>
    <g clip-path="url(#photo-page)">
      <circle cx="170" cy="230" r="188" fill="none" stroke="#ffffff" stroke-width="1.4"/>
      <circle cx="170" cy="240" r="160" fill="var(--gold)" opacity=".9"/>
      <circle cx="175" cy="230" r="118" fill="var(--navy)" opacity=".95"/>
    </g>
    <line x1="390" y1="0" x2="390" y2="552" stroke="#000" stroke-opacity=".12"/>
    <line x1="453" y1="118" x2="453" y2="210" stroke="var(--gold)" stroke-width="1.5"/>
    <line x1="453" y1="276" x2="453" y2="368" stroke="var(--gold)" stroke-width="1.5"/>
  </svg>

  <p class="section-badge">Partnership</p>

  <div class="timeline">
    <div class="timeline__item">
      <svg class="timeline__icon" viewBox="0 0 66 66" aria-hidden="true">
        <circle cx="33" cy="33" r="32" fill="#e4e4e4"/>
        <circle cx="33" cy="33" r="27" fill="#fafafa" stroke="var(--gold)" stroke-width="1.4"/>
        <circle cx="33" cy="31" r="9" fill="none" stroke="var(--navy)" stroke-width="1.6"/>
        <text x="33" y="35" text-anchor="middle" font-family="Poppins, sans-serif" font-size="11" font-weight="700" fill="var(--navy)">$</text>
        <path d="M20 44h26" stroke="var(--navy)" stroke-width="1.6"/>
      </svg>
      <h2 class="timeline__heading">The Partnership Overview</h2>
      <ul class="timeline__list">
        <li>Partnership initiation: February 2022</li>
        <li>Purpose: Implementing the Anti-Racism Road Map</li>
        <li>Backbone Support within the Collective Impact Model</li>
      </ul>
    </div>
    <div class="timeline__item">
      <svg class="timeline__icon" viewBox="0 0 66 66" aria-hidden="true">
        <circle cx="33" cy="33" r="32" fill="#e4e4e4"/>
        <circle cx="33" cy="33" r="27" fill="#fafafa" stroke="var(--gold)" stroke-width="1.4"/>
        <rect x="21" y="23" width="24" height="16" rx="2" fill="none" stroke="var(--navy)" stroke-width="1.6"/>
        <path d="M29 44h8M33 39v5" stroke="var(--navy)" stroke-width="1.6"/>
      </svg>
      <h2 class="timeline__heading">Project Key Assumptions</h2>
      <ul class="timeline__list">
        <li>Collective Impact Model guides strategy implementation</li>
        <li>Emphasis on change management and theories of change</li>
        <li>Commitment from BCN to prioritize and resource the initiative.</li>
      </ul>
    </div>
    <div class="timeline__item">
      <svg class="timeline__icon" viewBox="0 0 66 66" aria-hidden="true">
        <circle cx="33" cy="33" r="32" fill="#e4e4e4"/>
        <circle cx="33" cy="33" r="27" fill="#fafafa" stroke="var(--gold)" stroke-width="1.4"/>
        <circle cx="33" cy="30" r="6" fill="none" stroke="var(--navy)" stroke-width="1.6" stroke-dasharray="3 1.6"/>
        <circle cx="33" cy="30" r="2" fill="var(--navy)"/>
        <path d="M19 38q6 8 14 8t14-8" fill="none" stroke="var(--navy)" stroke-width="1.6"/>
      </svg>
      <h2 class="timeline__heading">The Role of The Halvorsen Circle, Inc</h2>
      <ul class="timeline__list">
        <li>Providing Backbone Support as per the Collective Impact Model</li>
        <li>Developing a sustainable strategic architecture</li>
        <li>Supporting the establishment of working teams and providing consultative support</li>
      </ul>
    </div>
  </div>
</section>

</body>
</html>
```